Labels design for a a range of food products

We are looking for labels design for a range of food product. The design should be the same for all the label with brown/black background and gold and white wording like the one attached.
The size and the content of the label will change depending on the different products.
I have also attached the logo to be used which is the logo "VELDORA" Marsk. You shall be using the black and gold version. Brighter/shining gold is better.
The first label to be designed is the one related a plastic tray like the one Cappelletti" file: IMG_20151231_021838
The second label to be designed is the one related to a bottle like the one "Olive Oil" file; IMG_20151231_021651
The third label to be designed is the one related to a jar like the one "Olive Taggiasche" file: IMG_20151231_021531 and IMG_20151231_021549
The fourth label to be designed is the one related to bag like the one IMG_20151231_021506
The fifth label to be designed is the one related to the bottle. IMG_20151231_021426_panorama
This files are only samples. I have attached a file excel "Texts for Labels" in which you will find the text to be applied for the labels.
In order to decide the best design a front and a back label should be provided.

Food Consumers

Product

• Front and Back Label
• Some pictures of the product on the label would be nice to have to recall what is inside.

```html
<!DOCTYPE html>
<html lang="it">
<head>
<meta charset="utf-8">
<title>VELDORA Marsk – Etichette</title>
<link rel="stylesheet" href="https://fonts.googleapis.com/css2?family=Alegreya:wght@400;500&display=swap">
<style>
  :root {
    --page: #ffffff;
    --label-dark: #2b0f12;
    --label-mid: #3a171b;
    --gold: #d6a94a;
    --cream: #f3e9dc;
    --edge: #1c080a;
    --meat-1: #c96a5c;
    --meat-2: #e6b3a3;
  }
  * { margin: 0; padding: 0; box-sizing: border-box; }
  html, body { width: 1200px; height: 1157px; overflow: hidden; background: var(--page); }
  body { position: relative; font-family: "Alegreya", Georgia, serif; color: var(--cream); }

  .label {
    position: absolute;
    background: linear-gradient(180deg, var(--label-mid), var(--label-dark));
    border: 2px solid var(--edge);
  }
  .brand { display: flex; flex-direction: column; align-items: center; gap: 8px; }
  .brand-dot { border-radius: 50%; border: 3px solid var(--gold); }
  .brand-name { color: var(--gold); font-weight: 500; text-align: center; line-height: 1.1; letter-spacing: 0.04em; }

  /* Bottle label */
  .label-bottle {
    left: 70px; top: 150px; width: 270px; height: 780px;
    display: flex; flex-direction: column; align-items: center; padding-top: 80px;
  }
  .label-bottle .brand-dot { width: 110px; height: 110px; }
  .label-bottle .brand-name { font-size: 22px; }
  .bottle-title { margin-top: 150px; font-size: 30px; line-height: 1.15; text-align: center; }
  .bottle-origin { margin-top: 30px; font-size: 19px; line-height: 1.5; text-align: center; color: var(--gold); }
  .bottle-note { margin-top: 34px; font-size: 18px; }
  .bottle-qty { margin-top: auto; margin-bottom: 70px; font-size: 24px; }

  /* Bag label */
  .label-bag {
    left: 420px; top: 300px; width: 320px; height: 250px;
    display: flex; flex-direction: column; align-items: center; padding-top: 24px;
  }
  .label-bag .brand-dot { width: 70px; height: 70px; }
  .label-bag .brand-name { font-size: 15px; }
  .bag-title { margin-top: 22px; font-size: 21px; }
  .bag-grade { margin-top: 6px; font-size: 16px; color: var(--gold); }
  .bag-qty { margin-top: 14px; font-size: 14px; }

  /* Tray label */
  .label-tray {
    left: 440px; top: 650px; width: 700px; height: 380px;
  }
  .label-tray .brand { position: absolute; left: 50%; top: 34px; transform: translateX(-50%); }
  .label-tray .brand-dot { width: 80px; height: 80px; }
  .label-tray .brand-name { font-size: 16px; }
  .tray-title { position: absolute; left: 0; right: 0; top: 170px; text-align: center; font-size: 48px; }
  .tray-sub { position: absolute; left: 40px; top: 60px; font-size: 22px; line-height: 1.2; color: var(--gold); }
  .tray-qty { position: absolute; left: 40px; top: 130px; font-size: 20px; }
  .tray-photo { position: absolute; left: 50%; bottom: 34px; transform: translateX(-50%); width: 220px; height: 100px; }
</style>
</head>
<body>

  <section class="label label-bottle" aria-label="Etichetta bottiglia olio">
    <div class="brand">
      <span class="brand-dot"></span>
      <span class="brand-name">VELDORA<br>Marsk</span>
    </div>
    <h1 class="bottle-title">Olio<br>extravergine<br>di oliva</h1>
    <p class="bottle-origin">Val di mazara DOP<br>Regione Sicilia</p>
    <p class="bottle-note">Estratto a freddo</p>
    <p class="bottle-qty">750 ml ℮</p>
  </section>

  <section class="label label-bag" aria-label="Etichetta busta funghi">
    <div class="brand">
      <span class="brand-dot"></span>
      <span class="brand-name">VELDORA Marsk</span>
    </div>
    <h2 class="bag-title">Funghi Porcinni secchi</h2>
    <p class="bag-grade">qualità extra</p>
    <p class="bag-qty">15 g ℮</p>
  </section>

  <section class="label label-tray" aria-label="Etichetta vaschetta cappelletti">
    <p class="tray-sub">con Prosciutto<br>di Parma</p>
    <p class="tray-qty">250 g ℮</p>
    <div class="brand">
      <span class="brand-dot"></span>
      <span class="brand-name">VELDORA Marsk</span>
    </div>
    <h2 class="tray-title">Capelletti</h2>
    <svg class="tray-photo" role="img" aria-label="Fette di prosciutto crudo con un rametto di rosmarino" viewBox="0 0 220 100">
      <defs>
        <linearGradient id="meat" x1="0" y1="0" x2="1" y2="1">
          <stop offset="0" stop-color="var(--meat-2)"/>
          <stop offset="1" stop-color="var(--meat-1)"/>
        </linearGradient>
      </defs>
      <rect width="220" height="100" rx="10" fill="url(#meat)"/>
    </svg>
  </section>

</body>
</html>
```